Design home page for quorvant.xyz

We’re seeking a sleek, lead-generation-focused single-page website for Quorvant.xyz that communicates our expertise in delivering high-intent leads to mid-sized businesses. The goal is to guide visitors toward scheduling a free consultation while emphasizing our performance-based approach and comprehensive service offerings.

Industry/Entity Type

Marketing

Number of Pages Required

1 page

Font styles to use
Sans Serif

Requirements
Must have
• content from https://pages.tillowmark.com/doc/d/7hRtWqLMPZX402KDNe19sbYQ3Vb8FkwTtPa6Ue2kHLSF/view?tab=t.0
Nice to have
• color pallet from here https://pages.tillowmark.com/doc/d/9kwebRA4-ZQTofCVyLpHmn52bPWJ83gdX5fjroarr7T/view?tab=t.0

```html
<!DOCTYPE html>
<html lang="en">
<head>
<meta charset="utf-8">
<title>quorvant.xyz — High-Intent Lead Generation</title>
<link rel="stylesheet" href="https://fonts.googleapis.com/css2?family=Roboto:wght@400;500;700&display=swap">
<style>
  :root {
    --red: #a8140f;
    --orange: #f5a000;
    --cream: #f6e8c3;
    --ink: #111111;
    --muted: #555555;
    --line: #ececec;
    --card-border: #dedede;
    --tile: #f2f2f2;
    --star: #f5b800;
    --white: #ffffff;
  }
  * { box-sizing: border-box; margin: 0; padding: 0; }
  html, body { width: 1200px; height: 2510px; overflow: hidden; background: var(--white); }
  body { font-family: "Roboto", Arial, sans-serif; color: var(--ink); position: relative; }
  .abs { position: absolute; }

  .site-header { left: 5px; top: 5px; width: 1190px; height: 66px; background: var(--cream); box-shadow: 0 1px 3px rgba(0,0,0,.08); }
  .brand { left: 314px; top: 16px; font-size: 25px; font-weight: 700; color: var(--ink); letter-spacing: .2px; }
  .nav { left: 505px; top: 24px; display: flex; gap: 34px; font-size: 13.5px; }
  .nav a { color: var(--ink); text-decoration: none; }

  .hero-title { left: 145px; top: 188px; width: 440px; font-size: 33px; line-height: 39px; font-weight: 700; color: var(--red); }
  .hero-text { left: 145px; top: 286px; width: 420px; font-size: 13px; line-height: 20px; }
  .btn { display: flex; align-items: center; justify-content: center; color: var(--white); font-size: 13px; font-weight: 500; border-radius: 5px; text-decoration: none; }
  .btn-primary { left: 145px; top: 346px; width: 188px; height: 39px; background: var(--orange); }
  .hero-art { left: 590px; top: 170px; width: 605px; height: 251px; background: linear-gradient(180deg, #f7f1e3 0%, #f7f1e3 52%, #e0a847 52%, #c98a3a 100%); }

  .divider { left: 5px; width: 1190px; height: 1px; background: var(--line); }

  .section-title { left: 0; width: 1200px; text-align: center; font-size: 33px; line-height: 41px; font-weight: 700; color: var(--red); }

  .service-card { width: 281px; height: 375px; border: 1px solid var(--card-border); border-radius: 3px; background: var(--white); overflow: hidden; }
  .service-card.wide { width: 910px; height: 346px; }
  .service-art { width: 100%; height: 281px; }
  .service-tag { position: absolute; left: 10px; top: 292px; font-size: 13px; color: #222; }
  .service-desc { position: absolute; left: 10px; top: 314px; width: 265px; font-size: 16.5px; line-height: 23px; font-weight: 500; }
  .wide .service-desc { width: 880px; }

  .section-sub { left: 395px; width: 410px; text-align: center; font-size: 13px; line-height: 20px; }

  .testimonial { width: 281px; height: 125px; background: var(--tile); border-radius: 2px; }
  .avatar { position: absolute; left: 13px; top: 12px; width: 26px; height: 26px; border-radius: 50%; background: #d8d8d8; }
  .t-name { position: absolute; left: 46px; top: 18px; font-size: 11.5px; font-weight: 500; }
  .stars { position: absolute; right: 13px; top: 17px; font-size: 10px; color: var(--star); letter-spacing: .5px; }
  .t-quote { position: absolute; left: 13px; top: 54px; width: 258px; font-size: 13px; line-height: 20px; }
  .t-quote span { display: block; white-space: nowrap; overflow: hidden; text-overflow: ellipsis; }

  .cta-title { left: 145px; top: 1960px; width: 680px; font-size: 33px; line-height: 39px; font-weight: 700; color: var(--red); }
  .cta-text { left: 145px; top: 2055px; font-size: 13px; }
  .cta-art { left: 907px; top: 1942px; width: 148px; height: 149px; background: linear-gradient(160deg, #f4e7c8 0%, #f2b233 60%, #c0291b 100%); }

  .field { width: 421px; }
  .field label { display: block; font-size: 11.5px; font-weight: 500; margin-bottom: 6px; }
  .field .input { height: 29px; border: 1px solid #d9d9d9; border-radius: 3px; font-size: 11.5px; color: #888; padding: 7px 9px; }
  .field .hint { font-size: 9px; color: var(--muted); margin-top: 5px; }
  .btn-submit { left: 501px; top: 2241px; width: 199px; height: 39px; background: var(--red); font-size: 13px; }

  .footer-copy { left: 267px; top: 2411px; font-size: 16.5px; }
  .footer-links { left: 661px; top: 2411px; font-size: 16.5px; }
  .footer-links a { color: var(--ink); text-decoration: none; }
</style>
</head>
<body>
  <header class="abs site-header">
    <div class="abs brand">quorvant.xyz</div>
    <nav class="abs nav">
      <a href="#home">Home</a><a href="#about">About</a><a href="#services">Services</a><a href="#testimonials">Testimonials</a><a href="#contact">Contact</a>
    </nav>
  </header>

  <section id="home">
    <h1 class="abs hero-title">High-Intent Leads Delivered Directly to Your Pipeline</h1>
    <p class="abs hero-text">Take the guesswork out of lead generation. We connect you with high-intent prospects who are genuinely interested in what you offer.</p>
    <a class="abs btn btn-primary" href="#contact">Schedule a Free Call Today</a>
    <div class="abs hero-art" role="img" aria-label="Illustration of business people meeting at a table with laptops"></div>
  </section>

  <div class="abs divider" style="top:500px"></div>

  <section id="services">
    <h2 class="abs section-title" style="top:552px">Comprehensive End-to-End<br>Lead Generation</h2>

    <article class="abs service-card" style="left:145px;top:680px">
      <div class="service-art" role="img" aria-label="Illustration of a creative content studio with ideas radiating outward" style="background:linear-gradient(180deg,#f4e6c6 0%,#f2ad2c 70%,#a8140f 100%)"></div>
      <p class="service-tag">Content Creation</p>
      <p class="service-desc">Unique and engaging content tailored for your audience</p>
    </article>
    <article class="abs service-card" style="left:460px;top:680px">
      <div class="service-art" role="img" aria-label="Illustration of a campaign control panel with upward arrows" style="background:linear-gradient(180deg,#f5a000 0%,#f4e6c6 45%,#3a3d45 80%,#b81e12 100%)"></div>
      <p class="service-tag">PPC Campaigns</p>
      <p class="service-desc">Strategically managed PPC campaigns to drive targeted traffic</p>
    </article>
    <article class="abs service-card" style="left:774px;top:680px">
      <div class="service-art" role="img" aria-label="Illustration of a network graph being examined with a magnifying glass" style="background:linear-gradient(180deg,#f7f0e1 0%,#f6dca0 60%,#e39a1f 100%)"></div>
      <p class="service-tag">SEO &amp; Social Media</p>
      <p class="service-desc">Optimized SEO and effective social media strategies</p>
    </article>

    <article class="abs service-card wide" style="left:145px;top:1089px">
      <div class="service-art" role="img" aria-label="Illustration of an analyst with headset monitoring live performance dashboards" style="background:linear-gradient(90deg,#f3a21c 0%,#3a3d45 35%,#f4e9d2 50%,#3a3d45 65%,#f3a21c 100%)"></div>
      <p class="service-tag">Real-Time Optimization</p>
      <p class="service-desc">Continuous monitoring and optimization for maximum results</p>
    </article>
  </section>

  <div class="abs divider" style="top:1485px"></div>

  <section id="testimonials">
    <h2 class="abs section-title" style="top:1537px">Client Testimonials</h2>
    <p class="abs section-sub" style="top:1599px">See what our satisfied clients have to say about our lead generation services</p>

    <article class="abs testimonial" style="left:145px;top:1701px">
      <span class="avatar"></span><span class="t-name">Alex J.</span><span class="stars">★★★★★</span>
      <p class="t-quote"><span>Quorvant.xyz has completely transformed</span><span>our lead generation efforts. We've seen a</span><span>35% increase in high-quality leads in just three months.</span></p>
    </article>
    <article class="abs testimonial" style="left:460px;top:1701px">
      <span class="avatar"></span><span class="t-name">Samantha L.</span><span class="stars">★★★★★</span>
      <p class="t-quote"><span>The team at Quorvant.xyz took care of</span><span>everything—from content to campaigns.</span><span>Their performance-based model meant we paid for results.</span></p>
    </article>
    <article class="abs testimonial" style="left:774px;top:1701px">
      <span class="avatar"></span><span class="t-name">Daniel G.</span><span class="stars">★★★★★</span>
      <p class="t-quote"><span>Working with Quorvant.xyz is like having</span><span>an in-house growth team. Their ability to</span><span>create and optimize content-driven campaigns is unmatched.</span></p>
    </article>
  </section>

  <div class="abs divider" style="top:1892px"></div>

  <section id="contact">
    <h2 class="abs cta-title">Ready to Unlock Scalable Growth for Your Business?</h2>
    <p class="abs cta-text">Schedule your free consultation call today to explore how we can help your business grow.</p>
    <div class="abs cta-art" role="img" aria-label="Illustration of a figure lifting a growth banner under a rising sun"></div>

    <div class="abs field" style="left:145px;top:2145px">
      <label>Full Name</label>
      <div class="input">Enter your full name</div>
      <div class="hint">Required</div>
    </div>
    <div class="abs field" style="left:634px;top:2145px">
      <label>Email Address</label>
      <div class="input">Enter your email address</div>
      <div class="hint">Required</div>
    </div>
    <a class="abs btn btn-submit" href="#contact">Schedule Your Free Call</a>
  </section>

  <div class="abs divider" style="top:2328px"></div>

  <footer>
    <p class="abs footer-copy">© 2023 quorvant.xyz. All rights reserved.</p>
    <p class="abs footer-links"><a href="#">Privacy Policy</a> | <a href="#">Terms of Service</a> | <a href="#">Sitemap</a></p>
  </footer>
</body>
</html>
```